Minimalistic logo and website for plovrek.com

My colleague and I just started a new company. We need a website to replace the placeholder at https://plovrek.com/

We need a onepager website. A logotype and color profiles. We like minimalism. Scandinavian design.

Below is just information about the company. You can rearrange it, add photos, emit stuff. Maybe even add stuff if you think it is necessary.

# About Plovrek
Plovrek builds critical applications to capture new markets, create modern services and captivate our customers in new and engaging ways. Creating effective and engaging solutions that truly work has always been Plovrek's core offering and is what makes us excited to work in digital. We are a forward thinking company embracing the opportunities of digital transformation and automations.

# Core services
Business automation
Application development and services for desktop and mobile
Interface Design and UX
Enterprise integrations

# Some more data
Plovrek was founded by Torvald Ekblom and Mikael Grundberg in 2021.
Linkedin: https://www.vendalink.com/company/58402917/admin/

# Inspiration
Minimal. Simple.
https://www.kvarnbyformverk.se/contact

Target Market(s)

Businesses

Industry/Entity Type

IT, business automation, data

Number of Pages Required

1 page

Font styles to use
Sans Serif

Colors

Designer to choose colors to be used in the design.

Requirements
Must have
• Onepage design. Minimalism.
Should not have
• Menus

```html
<!DOCTYPE html>
<html lang="en">
<head>
<meta charset="utf-8">
<title>Plovrek</title>
<link rel="stylesheet" href="https://fonts.googleapis.com/css2?family=Open+Sans:wght@400;600;700;800&display=swap">
<style>
:root{
  --navy:#070b1c;
  --navy-2:#0d1a3d;
  --glow:#2f6bff;
  --ink:#1b1b1f;
  --body:#3a3a40;
  --gold:#e0aa2c;
  --red:#c23b2e;
  --stone:#e9e9e5;
  --mist:#eef0fb;
  --white:#ffffff;
  --muted:#9aa0b4;
}
*{box-sizing:border-box;margin:0;padding:0}
html,body{width:1200px;height:4420px;overflow:hidden}
body{font-family:"Open Sans",Arial,sans-serif;color:var(--ink);background:var(--white)}
.btn{display:inline-block;background:var(--gold);color:var(--white);font-weight:700;font-size:13px;letter-spacing:.5px;text-transform:uppercase;padding:12px 30px;border-radius:24px;text-decoration:none}
.bar{width:56px;height:5px;background:var(--red);margin-bottom:18px}
h2{font-size:38px;font-weight:700;line-height:1.2;margin-bottom:18px}
.copy{font-size:15px;line-height:23px;color:var(--body);margin-bottom:40px}

/* hero */
.hero{position:relative;height:660px;background:var(--navy);color:var(--white);text-align:center;overflow:hidden}
.hero-art{position:absolute;inset:0;background:radial-gradient(ellipse 70% 28% at 50% 78%,rgba(47,107,255,.75),rgba(47,107,255,.15) 60%,transparent),linear-gradient(180deg,var(--navy) 0%,var(--navy-2) 70%,var(--navy) 100%)}
.topbar{position:absolute;top:0;left:0;right:0;display:flex;justify-content:space-between;align-items:center;padding:14px 56px}
.logo{font-size:30px;font-weight:700;letter-spacing:.5px;color:var(--white)}
.burger{width:36px;height:22px;display:flex;flex-direction:column;justify-content:space-between}
.burger span{height:3px;background:var(--white);border-radius:2px}
.hero-content{position:relative;padding-top:186px}
.hero h1{font-size:84px;font-weight:700;letter-spacing:3px;margin-bottom:22px}
.hero p{font-size:20px;line-height:30px;width:720px;margin:0 auto 34px}
.scroll-cue{position:absolute;left:50%;top:606px;margin-left:-12px}

/* about */
.about{position:relative;height:532px;padding:118px 112px 0}
.about-art{position:absolute;right:0;top:0;width:560px;height:532px;background:radial-gradient(ellipse at 80% 30%,rgba(47,107,255,.18),transparent 65%)}
.about-text{position:relative;width:830px}
.about h2{font-size:44px}

/* services */
.service{position:relative;height:600px;display:flex;align-items:center;padding:0 100px}
.service.stone{background:var(--stone)}
.service.mist{background:var(--mist)}
.service .art{width:480px;height:440px;border-radius:12px}
.stone .art{background:radial-gradient(circle at 50% 55%,#c9cde8,#e4e5ea 70%)}
.mist .art{background:radial-gradient(circle at 50% 55%,#c3ccf5,#e9ecfa 70%)}
.service .text{width:460px}
.service.art-left .text{margin-left:80px}
.service.art-right{justify-content:space-between;padding:0 112px}
.enterprise{height:712px}

/* clients */
.clients{height:360px;padding-top:72px;text-align:center}
.clients .bar{margin:0 auto 14px}
.clients h2{font-size:40px;margin-bottom:48px}
.client-grid{display:grid;grid-template-columns:repeat(5,1fr);row-gap:58px;padding:0 90px}
.client{font-size:24px;font-weight:700;color:var(--ink);display:flex;align-items:center;justify-content:center;gap:8px}
.client i{width:14px;height:14px;background:var(--ink);display:inline-block}

/* footer */
.footer{height:340px;background:var(--navy);color:var(--white);padding:40px 112px 0;position:relative}
.cols{display:flex}
.footer h4{font-size:14px;font-weight:700;letter-spacing:.5px;margin-bottom:14px}
.news{width:396px}
.fields{display:flex;gap:10px;margin-bottom:10px}
.field{background:var(--white);color:#888;font-size:11px;padding:8px 10px;flex:1}
.field.wide{width:330px;margin-bottom:12px}
.subscribe{display:block;width:330px;background:var(--gold);color:var(--white);font-size:14px;font-weight:700;text-align:center;padding:10px 0;border-radius:3px}
.links{width:168px}
.links ul{list-style:none;font-size:12px;line-height:22px}
.links li::before{content:"› ";color:var(--muted)}
.contact{font-size:12px;line-height:22px}
.contact div{display:flex;gap:8px;align-items:flex-start}
.socials{display:flex;gap:8px;margin-top:10px}
.socials span{width:22px;height:22px;border-radius:50%}
.rule{position:absolute;left:112px;right:112px;top:266px;border-top:1px solid #2a2f45}
.copyright{position:absolute;left:112px;top:290px;font-size:12px;color:#c9cbd6}
</style>
</head>
<body>

<header class="hero">
  <div class="hero-art" role="img" aria-label="Flowing blue light waves on a dark night background"></div>
  <div class="topbar">
    <div class="logo">plovrek</div>
    <div class="burger"><span></span><span></span><span></span></div>
  </div>
  <div class="hero-content">
    <h1>PLOVREK</h1>
    <p>Plovrek builds modern applications to capture new markets, create new services and captivate our clients in new and engaging ways.</p>
    <a class="btn" href="#">Get Started</a>
  </div>
  <svg class="scroll-cue" width="24" height="30" viewBox="0 0 24 30"><path d="M12 2v24M4 18l8 8 8-8" stroke="#fff" stroke-width="2" fill="none"/></svg>
</header>

<section class="about">
  <div class="about-art" role="img" aria-label="Faint network of connected points"></div>
  <div class="about-text">
    <div class="bar"></div>
    <h2>About Plovrek</h2>
    <p class="copy" style="font-size:17px;line-height:27px">Plovrek builds critical applications to capture new markets, create modern services and captivate our customers in new and engaging ways. Creating effective and engaging solutions that truly work has always been Plovrek's core offering and is what makes us excited to work in digital. We are a forward thinking company embracing the opportunities of digital transformation and automations.</p>
    <a class="btn" href="#">Learn More</a>
  </div>
</section>

<section class="service stone art-left">
  <div class="art" role="img" aria-label="Isometric illustration of people working with automated machines and screens"></div>
  <div class="text">
    <div class="bar"></div>
    <h2>Business Automation</h2>
    <p class="copy">Lorem ipsum dolor sit amet, consectetur adipiscing elit, sed do eiusmod tempor incididunt ut labore et dolore magna aliqua. Ut enim ad minim veniam, quis nostrud exercitation ullamco laboris nisi ut aliquip ex ea commodo consequat. Duis aute irure dolor in reprehenderit in voluptate velit esse cillum dolore eu fugiat nulla pariatur. Excepteur sint occaecat cupidatat non proident, sunt in culpa qui officia deserunt mollit anim id est laborum.</p>
    <a class="btn" href="#">Learn More</a>
  </div>
</section>

<section class="service mist art-right">
  <div class="text">
    <div class="bar"></div>
    <h2>Application Development And Services For Desktop And Mobile</h2>
    <p class="copy">Lorem ipsum dolor sit amet, consectetur adipiscing elit, sed do eiusmod tempor incididunt ut labore et dolore magna aliqua. Ut enim ad minim veniam, quis nostrud exercitation ullamco laboris nisi ut aliquip ex ea commodo consequat. Duis aute irure dolor in reprehenderit in voluptate velit ea.</p>
    <a class="btn" href="#">Learn More</a>
  </div>
  <div class="art" role="img" aria-label="Illustration of developers building apps around a large laptop and mobile devices"></div>
</section>

<section class="service stone art-left">
  <div class="art" role="img" aria-label="Illustration of designers arranging interface elements on a giant phone"></div>
  <div class="text">
    <div class="bar"></div>
    <h2>Interface Design and UX</h2>
    <p class="copy">Lorem ipsum dolor sit amet, consectetur adipiscing elit, sed do eiusmod tempor incididunt ut labore et dolore magna aliqua. Ut enim ad minim veniam, quis nostrud exercitation ullamco laboris nisi ut aliquip ex ea commodo consequat. Duis aute irure dolor in reprehenderit in voluptate velit esse cillum dolore eu fugiat nulla pariatur. Excepteur sint occaecat cupidatat non proident, sunt in culpa qui officia deserunt mollit anim id est laborum.</p>
    <a class="btn" href="#">Learn More</a>
  </div>
</section>

<section class="service mist art-right enterprise">
  <div class="text">
    <div class="bar"></div>
    <h2>Enterprise integrations</h2>
    <p class="copy">Lorem ipsum dolor sit amet, consectetur adipiscing elit, sed do eiusmod tempor incididunt ut labore et dolore magna aliqua. Ut enim ad minim veniam, quis nostrud exercitation ullamco laboris nisi ut aliquip ex ea commodo consequat. Duis aute irure dolor in reprehenderit in voluptate velit esse cillum dolore eu fugiat nulla pariatur. Excepteur sint occaecat cupidatat non proident, sunt in culpa qui officia deserunt mollit anim id est laborum.</p>
    <a class="btn" href="#">Learn More</a>
  </div>
  <div class="art" role="img" aria-label="Isometric illustration of people connecting servers, dashboards and data systems"></div>
</section>

<section class="clients">
  <div class="bar"></div>
  <h2>Clients</h2>
  <div class="client-grid">
    <div class="client"><i></i>Norvale</div>
    <div class="client">Brightwell</div>
    <div class="client">Kestrel</div>
    <div class="client">Tandor</div>
    <div class="client">Halvik</div>
    <div class="client">Corvane</div>
    <div class="client">Ostmark</div>
    <div class="client">Ridgeway</div>
    <div class="client">Alvena</div>
    <div class="client">Selberg</div>
  </div>
</section>

<footer class="footer">
  <div class="cols">
    <div class="news">
      <h4>GET INSIGHTS &amp; UPDATES</h4>
      <div class="fields" style="width:330px"><span class="field">Name</span><span class="field">Name</span></div>
      <div class="field wide">Email Address</div>
      <span class="subscribe">SUBSCRIBE</span>
    </div>
    <div class="links">
      <h4>QUICK LINKS</h4>
      <ul><li>Home</li><li>Who We Are</li><li>Services</li><li>Clients</li><li>Contact Us</li></ul>
    </div>
    <div class="links">
      <h4>OTHER LINKS</h4>
      <ul><li>Code Of Conduct</li><li>Privacy</li><li>Cookies Policy</li><li>Terms &amp; Conditions</li><li>Sitemap</li></ul>
    </div>
    <div class="contact">
      <h4>CONTACT INFO</h4>
      <div><svg width="12" height="14" viewBox="0 0 12 14"><path d="M6 0a5 5 0 0 0-5 5c0 4 5 9 5 9s5-5 5-9a5 5 0 0 0-5-5z" fill="#fff"/></svg><span>48 Ekdal Street,<br>Uppsala 75320</span></div>
      <div><svg width="12" height="12" viewBox="0 0 12 12"><path d="M2 1l2 0 1 3-1.5 1a7 7 0 0 0 3.5 3.5L8 7l3 1v2a1 1 0 0 1-1 1A10 10 0 0 1 1 2a1 1 0 0 1 1-1z" fill="#fff"/></svg><span>046-555-0182</span></div>
      <div><svg width="12" height="10" viewBox="0 0 12 10"><rect x=".5" y=".5" width="11" height="9" fill="none" stroke="#fff"/><path d="M.5.5L6 5l5.5-4.5" fill="none" stroke="#fff"/></svg><span>info@plovrek.com</span></div>
      <div class="socials"><span style="background:#1f5fd6"></span><span style="background:#e0245e"></span><span style="background:#2b7bd9"></span><span style="background:#c4302b"></span></div>
    </div>
  </div>
  <div class="rule"></div>
  <div class="copyright">© 2022. Plovrek. All Rights Reserved.</div>
</footer>

</body>
</html>
```